Ridgeline Build Network Inc. Letterhead

Creation of attractive and eye catching letterhead for a business start-up for the construction industry. Letterhead must relate to construction, but avoid standard hammer and tools in the design.
Updates

I forgot to add some details, sorry about that. Some pertinent info: Ph: 916-555-0148 ridgelinebuildnet.example 487 Willowmere Ave, Ste 210 Folsom, CA 95699 info@ridgelinebuildnet.example not sure if slogan should be in there" “Connecting construction professionals to create a purpose driven industry.” must be able to be used in word. Thanks!

```html
<!DOCTYPE html>
<html lang="en">
<head>
<meta charset="utf-8">
<title>Ridgeline Build Network Inc. Letterhead</title>
<link href="https://fonts.googleapis.com/css2?family=Montserrat:wght@400;600;800&display=swap" rel="stylesheet">
<style>
  :root {
    --backdrop: #666666;
    --paper: #ffffff;
    --navy: #262a6b;
    --red: #d0202a;
    --ink: #222222;
    --muted: #555555;
  }
  * { margin: 0; padding: 0; box-sizing: border-box; }
  html, body {
    width: 1200px;
    height: 800px;
    overflow: hidden;
    background: var(--backdrop);
    font-family: "Montserrat", Arial, sans-serif;
  }
  .letterhead {
    position: absolute;
    left: 330px;
    top: 18px;
    width: 540px;
    height: 764px;
    background: var(--paper);
    overflow: hidden;
  }
  .brand {
    position: absolute;
    top: 70px;
    right: 46px;
    display: flex;
    align-items: center;
    gap: 7px;
  }
  .brand-square {
    width: 12px;
    height: 12px;
    background: var(--red);
  }
  .brand-name {
    font-size: 11px;
    font-weight: 800;
    letter-spacing: 0.06em;
    text-transform: uppercase;
    color: var(--navy);
    white-space: nowrap;
  }
  .contact {
    position: absolute;
    left: 34px;
    top: 620px;
    color: var(--ink);
  }
  .contact-name {
    font-size: 9px;
    font-weight: 800;
    text-transform: uppercase;
    letter-spacing: 0.02em;
    margin-bottom: 4px;
  }
  .contact-line {
    font-size: 6.5px;
    font-weight: 400;
    color: var(--muted);
    line-height: 1.45;
    white-space: nowrap;
  }
  .footer-rule {
    position: absolute;
    left: 0;
    bottom: 0;
    width: 540px;
    height: 18px;
    display: flex;
    gap: 8px;
  }
  .footer-rule-navy {
    flex: 0 0 380px;
    background: var(--navy);
  }
  .footer-rule-red {
    flex: 1 1 auto;
    background: var(--red);
  }
</style>
</head>
<body>
  <main class="letterhead">
    <header class="brand">
      <span class="brand-square"></span>
      <span class="brand-name">Ridgeline Build Network</span>
    </header>

    <section class="contact">
      <p class="contact-name">Ridgeline Build Network Inc.</p>
      <p class="contact-line">487 Willowmere Ave, Ste 210, Folsom, CA 95699</p>
      <p class="contact-line">Ph: 916-555-0148</p>
      <p class="contact-line">info@ridgelinebuildnet.example | ridgelinebuildnet.example</p>
    </section>

    <footer class="footer-rule" aria-hidden="true">
      <span class="footer-rule-navy"></span>
      <span class="footer-rule-red"></span>
    </footer>
  </main>
</body>
</html>
```